Australian Wine export company Need a Wine label design

We need a wine label design for a new branded Australian wine based in South Australia called " KESTRELMOOR " .
We will use this brand name ' KESTRELMOOR' to marketing Australian Red wine and White wine into Chinese Market.
We would like to see the label designs that look classic and make consumers feel this is a superior quality Australian wine.
This label is to promote AUSTRALIAN WINE, need wine related and country related theme, need to give the consumer first impression that this wine is from AUSTRALIA.

Thanks

The following information are required to be presented on the wine label:

1) Brand Name: Kestrelmoor
2) Logo
3) Year of Vintage
4) Varietal
5) Place of production: South Australia
6) Fine Wine of Australia

Thanks.

Target Market(s)

Chinese market

Industry/Entity Type

Marketing

Requirements
Must have
• Need label design and renderings on the bottles.
Nice to have
• Label make consumers feel this is a superior quality Australian Wine.

```html
<!DOCTYPE html>
<html lang="en">
<head>
<meta charset="utf-8">
<title>Kestrelmoor Wine Labels</title>
<link href="https://fonts.googleapis.com/css2?family=Bodoni+Moda:wght@400;500&family=Libre+Caslon+Text&display=swap" rel="stylesheet">
<style>
  :root {
    --canvas: #ffffff;
    --label-paper: #f4f3ef;
    --label-edge: #e4e2dc;
    --ink: #2a2a28;
    --gold-dark: #8a7a12;
    --gold-mid: #c2ae2a;
    --gold-light: #e3d46a;
    --band-text: #f7f1cf;
  }
  * { box-sizing: border-box; margin: 0; padding: 0; }
  html, body {
    width: 1200px;
    height: 900px;
    overflow: hidden;
    background: var(--canvas);
  }
  .range {
    position: relative;
    width: 1200px;
    height: 900px;
  }
  .label {
    position: absolute;
    top: 388px;
    width: 210px;
    height: 260px;
    background: linear-gradient(90deg, var(--label-edge) 0%, var(--label-paper) 14%, #fbfaf7 50%, var(--label-paper) 86%, var(--label-edge) 100%);
    color: var(--ink);
    text-align: center;
  }
  .label--chardonnay { left: 243px; }
  .label--rose { left: 522px; }
  .label--cabernet { left: 801px; }

  .brand-mark {
    position: absolute;
    top: 44px;
    left: 50%;
    width: 14px;
    height: 14px;
    margin-left: -7px;
    border-radius: 50%;
    background: linear-gradient(135deg, var(--gold-light), var(--gold-dark));
  }
  .brand-name {
    position: absolute;
    top: 80px;
    left: 0;
    right: 0;
    font-family: "Bodoni Moda", "Times New Roman", serif;
    font-weight: 400;
    font-size: 16px;
    letter-spacing: 2.6px;
    color: var(--ink);
  }
  .wine-details {
    position: absolute;
    top: 127px;
    left: 0;
    right: 0;
    font-family: "Libre Caslon Text", "Times New Roman", serif;
    font-size: 11.5px;
    line-height: 19px;
    letter-spacing: 0.5px;
  }
  .volume {
    position: absolute;
    top: 212px;
    right: 10px;
    font-family: "Libre Caslon Text", "Times New Roman", serif;
    font-size: 9px;
  }
  .gold-band {
    position: absolute;
    top: 232px;
    left: 0;
    right: 0;
    height: 28px;
    background: linear-gradient(180deg, var(--gold-dark) 0%, var(--gold-mid) 35%, var(--gold-light) 55%, var(--gold-mid) 75%, var(--gold-dark) 100%);
    font-family: "Libre Caslon Text", "Times New Roman", serif;
    font-size: 7px;
    letter-spacing: 1px;
    line-height: 28px;
    color: var(--band-text);
    text-transform: uppercase;
  }
</style>
</head>
<body>
<main class="range">
  <section class="label label--chardonnay">
    <span class="brand-mark"></span>
    <h1 class="brand-name">KESTRELMOOR</h1>
    <p class="wine-details">South Australia<br>Chardonnay<br>2012</p>
    <p class="volume">750ml</p>
    <p class="gold-band">Fine Wine of Australia</p>
  </section>

  <section class="label label--rose">
    <span class="brand-mark"></span>
    <h1 class="brand-name">KESTRELMOOR</h1>
    <p class="wine-details">South Australia<br>Rosé<br>2012</p>
    <p class="volume">750ml</p>
    <p class="gold-band">Fine Wine of Australia</p>
  </section>

  <section class="label label--cabernet">
    <span class="brand-mark"></span>
    <h1 class="brand-name">KESTRELMOOR</h1>
    <p class="wine-details">South Australia<br>Cabernet Sauvignon<br>2012</p>
    <p class="volume">750ml</p>
    <p class="gold-band">Fine Wine of Australia</p>
  </section>
</main>
</body>
</html>
```